Business Card Design Project

We need a business card to reflect the design of our website - just so it all ties in - it has a retro feel and can be found at http://www.velorasoulpair.com
We will need our phone 0437 215 964
Web address, and email velorapair@fernmail.com included
Our catch cry is "Classic Cocktail Music"
Perfect Live Music for Private & Corporate Events, Weddings and Dinner Music
Our names should be included :-
Maribel Thorne / piano & Dennis Holloway / bass
I am now also including our logo so that it can be included (in part or whole) somehow in the design
My partner thinks we should include our logo in some form in the design of the card - i will attach this here for you. I will attach eps but if you prefer another format please let me know
Regards
Mari

```html
<!DOCTYPE html>
<html lang="en">
<head>
<meta charset="utf-8">
<title>Velora Duo – Business Cards</title>
<link rel="stylesheet" href="https://fonts.googleapis.com/css2?family=Poiret+One&family=Righteous&family=Oswald:wght@500&family=Open+Sans:wght@400;600&display=swap">
<style>
  :root {
    --backdrop: #d9d3c4;
    --teal: #8fc8ca;
    --teal-deep: #7bb7ba;
    --cream: #e8e5dd;
    --orange: #dc5b3b;
    --charcoal: #58585b;
    --ink: #464646;
    --ribbon: #f1ecd9;
    --ribbon-fold: #c9c1a6;
    --dot: #bdb8ab;
  }
  * { box-sizing: border-box; margin: 0; padding: 0; }
  html, body { width: 1200px; height: 800px; overflow: hidden; }
  body { background: var(--backdrop); position: relative; font-family: "Open Sans", sans-serif; color: var(--ink); }

  .card {
    position: absolute; width: 580px; height: 331px; overflow: hidden;
    background: var(--cream); border-radius: 3px;
    box-shadow: 0 10px 24px rgba(60,50,30,.28);
  }
  .card--details { left: 50px; top: 50px; }
  .card--front { left: 570px; top: 420px; }

  .band-top { position: absolute; left: 0; top: 0; width: 100%; background: var(--teal); }
  .band-top::after {
    content: ""; position: absolute; left: 0; right: 0; bottom: 5px;
    border-bottom: 1px dashed rgba(255,255,255,.6);
  }
  .card--details .band-top { height: 100px; }
  .card--front .band-top { height: 90px; }

  .band-bottom { position: absolute; left: 0; bottom: 0; width: 100%; background: var(--orange); }
  .card--details .band-bottom { height: 12px; }
  .card--front .band-bottom { height: 74px; }

  .emblem {
    position: absolute; width: 88px; height: 88px; border-radius: 50%;
    background: var(--charcoal); border: 5px solid var(--teal-deep);
    box-shadow: 0 0 0 2px rgba(255,255,255,.35);
  }
  .card--details .emblem { left: 186px; top: 52px; }
  .card--front .emblem { left: 246px; top: 42px; }

  .brand {
    position: absolute; font-family: "Poiret One", sans-serif; font-size: 28px;
    letter-spacing: 3px; color: var(--teal-deep); white-space: nowrap; line-height: 1;
  }
  .card--details .brand { left: 150px; top: 148px; }
  .card--front .brand { left: 0; width: 100%; text-align: center; top: 138px; }

  .ribbon { position: absolute; }
  .card--details .ribbon { left: 124px; top: 180px; width: 216px; height: 32px; }
  .card--front .ribbon { left: 140px; top: 174px; width: 300px; height: 42px; }
  .ribbon__label {
    position: absolute; inset: 0; display: flex; align-items: center; justify-content: center;
    font-family: "Righteous", sans-serif; color: #2e2e2e; letter-spacing: 1px; white-space: nowrap;
  }
  .card--details .ribbon__label { font-size: 14px; }
  .card--front .ribbon__label { font-size: 20px; }

  .dots { position: absolute; height: 0; border-top: 3px dotted var(--dot); }
  .card--details .dots { left: 20px; width: 170px; top: 232px; }
  .card--front .dots--left { left: 30px; width: 110px; top: 236px; }
  .card--front .dots--right { right: 30px; width: 110px; top: 236px; }

  .contact-list { position: absolute; left: 200px; top: 222px; list-style: none; }
  .contact-list li { display: flex; align-items: center; height: 22px; font-size: 11px; white-space: nowrap; }
  .contact-list .icon {
    width: 17px; height: 17px; border-radius: 50%; background: var(--orange);
    margin-right: 7px; display: flex; align-items: center; justify-content: center; flex: none;
  }
  .contact-list .label { font-family: "Oswald", sans-serif; font-weight: 500; letter-spacing: .5px; color: #2f2f2f; margin-right: 4px; }

  .site-line {
    position: absolute; left: 0; width: 100%; top: 226px; text-align: center;
    font-size: 14px; letter-spacing: 1.5px; color: var(--ink); line-height: 20px;
  }

  .social {
    position: absolute; bottom: 0; left: 0; width: 100%; height: 74px;
    display: flex; align-items: center; justify-content: center; gap: 36px;
    color: #fbe6dc; font-weight: 600; font-size: 15px;
  }
  .social__item { display: flex; align-items: center; gap: 10px; }
  .social__square { width: 22px; height: 22px; background: #f7e4da; border-radius: 3px; }
  .social__divider { width: 1px; height: 22px; background: rgba(255,255,255,.6); }
</style>
</head>
<body>

  <section class="card card--details" aria-label="Velora Duo contact card">
    <div class="band-top"></div>
    <div class="band-bottom"></div>
    <div class="emblem"></div>
    <div class="brand">VELORA DUO</div>
    <div class="ribbon">
      <svg width="100%" height="100%" viewBox="0 0 216 32" preserveAspectRatio="none">
        <polygon points="0,8 20,8 20,31 0,31 8,19" fill="var(--ribbon-fold)"/>
        <polygon points="216,1 196,1 196,24 216,24 208,12" fill="var(--ribbon-fold)"/>
        <polygon points="12,4 204,0 204,25 12,29" fill="var(--ribbon)"/>
      </svg>
      <span class="ribbon__label">CLASSIC COCKTAIL MUSIC</span>
    </div>
    <div class="dots"></div>
    <ul class="contact-list">
      <li>
        <span class="icon"><svg width="10" height="10" viewBox="0 0 10 10"><circle cx="5" cy="3" r="2.2" fill="#fff"/><path d="M1 10 Q5 4 9 10Z" fill="#fff"/></svg></span>
        <span class="label">TEAM :</span> Maribel Thorne / Piano &amp; Dennis Holloway / Bass
      </li>
      <li>
        <span class="icon"><svg width="10" height="10" viewBox="0 0 10 10"><path d="M2 1 L4 1 L4.6 3.4 L3.4 4.2 Q4.4 6 5.8 6.6 L6.6 5.4 L9 6 L9 8 Q8 9.4 6 9 Q1.5 7 1 3 Q0.8 1.5 2 1Z" fill="#fff"/></svg></span>
        <span class="label">PHONE :</span> 0437 215 964
      </li>
      <li>
        <span class="icon"><svg width="10" height="8" viewBox="0 0 10 8"><rect x="0.5" y="0.5" width="9" height="7" fill="none" stroke="#fff"/><path d="M0.5 0.5 L5 4.5 L9.5 0.5" fill="none" stroke="#fff"/></svg></span>
        <span class="label">EMAIL :</span> velorapair@fernmail.com
      </li>
      <li>
        <span class="icon"><svg width="10" height="10" viewBox="0 0 10 10"><circle cx="5" cy="5" r="4" fill="none" stroke="#fff"/><path d="M1 5 H9 M5 1 V9" stroke="#fff"/></svg></span>
        <span class="label">WEBSITE :</span> www.velorasoulpair.com
      </li>
    </ul>
  </section>

  <section class="card card--front" aria-label="Velora Duo front card">
    <div class="band-top"></div>
    <div class="band-bottom"></div>
    <div class="emblem"></div>
    <div class="brand">VELORA DUO</div>
    <div class="ribbon">
      <svg width="100%" height="100%" viewBox="0 0 300 42" preserveAspectRatio="none">
        <polygon points="0,10 28,10 28,41 0,41 10,25" fill="var(--ribbon-fold)"/>
        <polygon points="300,1 272,1 272,32 300,32 290,16" fill="var(--ribbon-fold)"/>
        <polygon points="16,6 284,0 284,32 16,38" fill="var(--ribbon)"/>
      </svg>
      <span class="ribbon__label">CLASSIC COCKTAIL MUSIC</span>
    </div>
    <div class="site-line">WWW.VELORASOULPAIR.COM</div>
    <div class="dots dots--left"></div>
    <div class="dots dots--right"></div>
    <div class="social">
      <span class="social__item"><span class="social__square"></span>Friendwall.com/veloraduo</span>
      <span class="social__divider"></span>
      <span class="social__item"><span class="social__square"></span>Chirper.com/veloraduo</span>
    </div>
  </section>

</body>
</html>
```